Zarvo! Next Steps?, Bail Bond Company Check-in App , Court date, Court Reminders, Payments

Zarvo!
Next Steps?
WINNER OF THIS CONTEST WILL HAVE OPPORTUNITY TO DESIGN CUSTOMIZE SOME OUR COMPANY PAGES AFTER CONTEST!
Check-in with your Bail agent via pic/video
Receive Court reminders
Make a payments

Basically this app is a portal to 3rd party bail companies.
The idea is for the person whom makes bail downloads the Zarvo app from App Store.
Then they select a bail bond company.
This would be similar to a restaurant, real estate agent, insurance agent,,app where we could populate bail bond companies by client location or by typing in name of bail company.
We would like the ability to customize each bail bond company landing pages but are open to a global concept. when you click the bail bond company location it would have the logos for that company so the bail bond company screens would need to be customizeble
The app will require a photo or video check-in that is date and time
stamped with a gps location stored in check-in history
Check-in can be scheduled or random or voluntary
Voluntary and Scheduled Check-ins would require check-in button
Random would be via alert or text

The app should be able to receive court date updates
The app should allow clients to make payments to bail bond company
we need
ZARVO! landing page
client registration screens, check-in screens, available bail bond company screens for client to choose from
client registration page should include
name
email address
phone number
picture
home address
work address
date of birth
this app is different from our u-trak app. this is a bail bond check-in app for third party bail bond companies.
landing page should be ZARVO! Next Steps?
ZARVO ! Registration
Find your bail bond Company should list bail bond companies near me and search bar for searching bail bond companies by name
Next landing pages would be customizable for the third party bail bond companies
these would include pages for
check-ins via pics/videos
payment page
court reminders
contact information for bail bond companies
Zarvo Pages include
initial landing page
registration page
search bail companies

Bail bond company pages should include
Bali bond company landing page
Use KELNOR BAIL BOND COMPANY as example
contact information for bail company
check-in page
payment page
court reminder page
Updates

Low designer entries

Low designer entries

Sick

Sick

Sick

Target Market(s)

Court Defendants, Probation ,jails, sheriffs, judges, attorneys

Industry/Entity Type

justice, law enforcement, courts,

Requirements
Must have
• Check-in via pic/video, ability to receive court date reminders, make paymentswe need client registration screens, check-in screens, available bail bond company screens for client to choose from
Nice to have
• Professional easy to navigate intuitive customizable to 3rd party bail bond companies, logos,phone numbers etc.
Should not have
• unprofessional graphics,

```html
<!DOCTYPE html>
<html lang="en">
<head>
<meta charset="utf-8">
<title>Zarvo! Next Steps? — App Screens</title>
<link href="https://fonts.googleapis.com/css2?family=Questrial&family=Roboto:wght@400;500;700&display=swap" rel="stylesheet">
<style>
:root{
  --bg:#7f7f7f;
  --navy:#0f1c58;
  --navy-deep:#0a1446;
  --band-light:#1f5fbf;
  --brand:#1a6aa0;
  --button:#0b8bc3;
  --ink:#1c1c1c;
  --muted:#555;
  --line:#cfcfcf;
  --link-blue:#1aa0d6;
  --icon-grey:#9a9a9a;
  --white:#fff;
}
*{box-sizing:border-box;margin:0;padding:0}
html,body{width:955px;height:1200px;overflow:hidden}
body{background:var(--bg);font-family:"Roboto",sans-serif;color:var(--ink);position:relative}
.screen{position:absolute;overflow:hidden;
  background:linear-gradient(160deg,var(--navy-deep) 0%,var(--band-light) 45%,var(--navy) 100%)}
.panel{position:absolute;background:var(--white)}
.abs{position:absolute}
.logo{font-family:"Questrial",sans-serif;color:var(--brand);font-size:27px;letter-spacing:1.5px;white-space:nowrap}
.title-bar{position:absolute;left:0;right:0;background:var(--navy);color:var(--white);font-weight:700;display:flex;align-items:center}
.field{position:absolute;border:1px solid #bdbdbd;background:var(--white);display:flex;align-items:center;justify-content:space-between;font-size:9.5px;color:#222}
.btn{position:absolute;background:var(--button);color:var(--white);border-radius:20px;font-weight:700;display:flex;align-items:center;justify-content:center}
.photo{position:absolute}
.header-icons{position:absolute;display:flex;gap:15px}

/* login */
.login .label{position:absolute;left:17px;font-size:9.5px;letter-spacing:.3px}
.login .field{left:17px;width:200px;height:38px;padding:0 10px 0 20px;color:#999}
.social{position:absolute;top:392px;left:0;width:100%;display:flex;justify-content:center;gap:7px}
.social span{width:25px;height:25px;border-radius:50%;color:var(--white);font-size:5.5px;font-weight:700;display:flex;align-items:center;justify-content:center}

/* list */
.company{position:absolute;left:4px;width:224px;height:99.5px;border-bottom:1px solid var(--line)}
.company .photo{left:9px;top:13px;width:79px;height:71px}
.company .name{position:absolute;left:103px;top:15px;font-size:11.5px;font-weight:500}
.company .desc{position:absolute;left:103px;top:34px;font-size:8px;line-height:12px;color:#333;width:100px}
.phone-row{display:flex;align-items:center;gap:5px;color:var(--link-blue);font-size:9.5px;font-weight:500;letter-spacing:.3px}
.company .phone-row{position:absolute;left:103px;top:69px}
.dot{width:15px;height:15px;border-radius:50%;background:#165e94;display:flex;align-items:center;justify-content:center}

/* detail */
.about{position:absolute;left:13px;width:208px;top:329px;font-size:7.6px;line-height:16.1px;color:#444;text-align:justify}
.history{position:absolute;left:16px;top:702px;list-style:none}
.history li{font-size:10.5px;line-height:19.5px;color:#555;text-decoration:underline;text-underline-offset:2px}
.cards{position:absolute;left:16px;top:914px;display:flex;gap:7px}
.cards span{width:26px;height:17px;border:1px solid #d6d6d6;background:#f4f4f4;font-size:5.5px;font-weight:700;color:#1a3b8a;display:flex;align-items:center;justify-content:center}
</style>
</head>
<body>

<!-- Login screen -->
<section class="screen login" style="left:97px;top:117px;width:226px;height:496px">
  <div class="panel" style="left:0;top:18px;width:226px;height:420px">
    <div class="logo abs" style="top:16px;width:100%;text-align:center">ZARVO!</div>
    <div class="title-bar" style="top:74px;height:34px;justify-content:center;font-size:21px">LOGIN</div>
    <div class="label" style="top:124px">USERNAME</div>
    <div class="field" style="top:139px"><span>riley@mailbox.test</span>
      <svg width="9" height="9" viewBox="0 0 10 10"><circle cx="5" cy="3" r="2.4" fill="#999"/><path d="M0.5 10a4.5 4 0 0 1 9 0z" fill="#999"/></svg></div>
    <div class="label" style="top:198px">PASSWORD</div>
    <div class="field" style="top:212px;letter-spacing:3px"><span>* * * * * * * *</span>
      <svg width="9" height="10" viewBox="0 0 9 10"><path d="M2 4V3a2.5 2.5 0 0 1 5 0v1" fill="none" stroke="#999" stroke-width="1.2"/><rect x="0.5" y="4" width="8" height="6" fill="#999"/></svg></div>
    <div class="abs" style="top:268px;right:9px;font-size:9.5px;text-decoration:underline">Fogot Password?</div>
    <div class="btn" style="left:61px;top:284px;width:104px;height:38px;font-size:15px;font-weight:500">LOGIN</div>
    <div class="abs" style="top:334px;width:100%;text-align:center;font-size:11.5px;font-weight:500">Or</div>
    <div class="abs" style="top:354px;width:100%;text-align:center;font-size:12px;font-weight:500">Sign up Using</div>
    <div class="social">
      <span style="background:#3b5898">Linkora</span>
      <span style="background:#2ea3e6">Chirpo</span>
      <span style="background:#d34836">Gleamo</span>
    </div>
  </div>
</section>

<!-- Company list screen -->
<section class="screen list" style="left:350px;top:106px;width:252px;height:989px">
  <div class="panel" style="left:13px;top:17px;width:228px;height:947px">
    <div class="logo abs" style="left:14px;top:16px">ZARVO!</div>
    <div class="header-icons" style="left:171px;top:24px">
      <svg width="14" height="14" viewBox="0 0 10 10"><circle cx="5" cy="3" r="2.4" fill="var(--icon-grey)"/><path d="M0.5 10a4.5 4 0 0 1 9 0z" fill="var(--icon-grey)"/></svg>
      <svg width="14" height="14" viewBox="0 0 10 10"><path d="M5 1a3 3 0 0 1 3 3v3l1 1H1l1-1V4a3 3 0 0 1 3-3z" fill="var(--icon-grey)"/><circle cx="5" cy="9.2" r="0.9" fill="var(--icon-grey)"/></svg>
    </div>
    <div class="title-bar" style="top:56px;height:35px;padding-left:19px;font-size:19px">LIST OF COMPANIES</div>
    <div class="field" style="left:13px;top:100px;width:201px;height:37px;padding:0 15px 0 20px"><span>Client Location</span>
      <svg width="8" height="5" viewBox="0 0 8 5"><path d="M0 0h8L4 5z" fill="#111"/></svg></div>
    <div class="field" style="left:13px;top:144px;width:201px;height:37px;padding:0 20px"><span>Name of the Bail Company</span></div>

    <div class="company" style="top:188px"><div class="photo" role="img" aria-label="Photo of a glass office building" style="background:linear-gradient(160deg,#bfe1f5,#2f7fc0 60%,#5d8a55)"></div><div class="name">Sed ut perspiciatis</div><div class="desc">Lorem ipsum dolor sit amet, consectetur</div><div class="phone-row"><span class="dot"><svg width="8" height="8" viewBox="0 0 10 10"><path d="M2 1l2 2-1 1.5a6 6 0 0 0 2.5 2.5L7 6l2 2-1.5 1.5C4 9 1 6 .5 2.5z" fill="#fff"/></svg></span>+1 555 010 2040</div></div>
    <div class="company" style="top:287.5px"><div class="photo" role="img" aria-label="Photo of a dark glass office block at dusk" style="background:linear-gradient(170deg,#a9c6dc,#334a6a 55%,#8b7b6b)"></div><div class="name">Sed ut perspiciatis</div><div class="desc">Lorem ipsum dolor sit amet, consectetur</div><div class="phone-row"><span class="dot"><svg width="8" height="8" viewBox="0 0 10 10"><path d="M2 1l2 2-1 1.5a6 6 0 0 0 2.5 2.5L7 6l2 2-1.5 1.5C4 9 1 6 .5 2.5z" fill="#fff"/></svg></span>+1 555 010 2040</div></div>
    <div class="company" style="top:387px"><div class="photo" role="img" aria-label="Photo of a modern apartment building corner" style="background:linear-gradient(150deg,#6fb0e8,#3f6ea8 45%,#8a5a3e)"></div><div class="name">Sed ut perspiciatis</div><div class="desc">Lorem ipsum dolor sit amet, consectetur</div><div class="phone-row"><span class="dot"><svg width="8" height="8" viewBox="0 0 10 10"><path d="M2 1l2 2-1 1.5a6 6 0 0 0 2.5 2.5L7 6l2 2-1.5 1.5C4 9 1 6 .5 2.5z" fill="#fff"/></svg></span>+1 555 010 2040</div></div>
    <div class="company" style="top:486.5px"><div class="photo" role="img" aria-label="Photo of a light office building" style="background:linear-gradient(160deg,#d5e4f2,#9fb3c6 55%,#6e7f63)"></div><div class="name">Sed ut perspiciatis</div><div class="desc">Lorem ipsum dolor sit amet, consectetur</div><div class="phone-row"><span class="dot"><svg width="8" height="8" viewBox="0 0 10 10"><path d="M2 1l2 2-1 1.5a6 6 0 0 0 2.5 2.5L7 6l2 2-1.5 1.5C4 9 1 6 .5 2.5z" fill="#fff"/></svg></span>+1 555 010 2040</div></div>
    <div class="company" style="top:586px"><div class="photo" role="img" aria-label="Photo of a city skyline with a tall tower" style="background:linear-gradient(180deg,#2f7fd0,#7fb4e6 55%,#5a4a3e)"></div><div class="name">Sed ut perspiciatis</div><div class="desc">Lorem ipsum dolor sit amet, consectetur</div><div class="phone-row"><span class="dot"><svg width="8" height="8" viewBox="0 0 10 10"><path d="M2 1l2 2-1 1.5a6 6 0 0 0 2.5 2.5L7 6l2 2-1.5 1.5C4 9 1 6 .5 2.5z" fill="#fff"/></svg></span>+1 555 010 2040</div></div>
    <div class="company" style="top:685.5px"><div class="photo" role="img" aria-label="Photo of glass office buildings" style="background:linear-gradient(165deg,#6a94c0,#2c4a72 55%,#5f7a4a)"></div><div class="name">Sed ut perspiciatis</div><div class="desc">Lorem ipsum dolor sit amet, consectetur</div><div class="phone-row"><span class="dot"><svg width="8" height="8" viewBox="0 0 10 10"><path d="M2 1l2 2-1 1.5a6 6 0 0 0 2.5 2.5L7 6l2 2-1.5 1.5C4 9 1 6 .5 2.5z" fill="#fff"/></svg></span>+1 555 010 2040</div></div>
    <div class="company" style="top:785px"><div class="photo" role="img" aria-label="Photo of a white residential building" style="background:linear-gradient(150deg,#3f86d6,#a9c9ea 50%,#e8e8e8)"></div><div class="name">Sed ut perspiciatis</div><div class="desc">Lorem ipsum dolor sit amet, consectetur</div><div class="phone-row"><span class="dot"><svg width="8" height="8" viewBox="0 0 10 10"><path d="M2 1l2 2-1 1.5a6 6 0 0 0 2.5 2.5L7 6l2 2-1.5 1.5C4 9 1 6 .5 2.5z" fill="#fff"/></svg></span>+1 555 010 2040</div></div>

    <div class="btn" style="left:61px;top:896px;width:105px;height:38px;font-size:12px">VIEW MORE</div>
  </div>
</section>

<!-- Company detail screen -->
<section class="screen detail" style="left:619px;top:106px;width:252px;height:989px">
  <div class="panel" style="left:13px;top:17px;width:228px;height:947px">
    <div class="logo abs" style="left:14px;top:16px">ZARVO!</div>
    <div class="header-icons" style="left:171px;top:24px">
      <svg width="14" height="14" viewBox="0 0 10 10"><circle cx="5" cy="3" r="2.4" fill="var(--icon-grey)"/><path d="M0.5 10a4.5 4 0 0 1 9 0z" fill="var(--icon-grey)"/></svg>
      <svg width="14" height="14" viewBox="0 0 10 10"><path d="M5 1a3 3 0 0 1 3 3v3l1 1H1l1-1V4a3 3 0 0 1 3-3z" fill="var(--icon-grey)"/><circle cx="5" cy="9.2" r="0.9" fill="var(--icon-grey)"/></svg>
    </div>
    <div class="photo" role="img" aria-label="Photo of the bail bond company's glass office building" style="left:6px;top:56px;width:214px;height:189px;background:linear-gradient(160deg,#e6f0f8 0%,#8cc0e6 35%,#2a72b8 65%,#6f8f5c 100%)"></div>
    <div class="abs" style="left:12px;top:258px;font-size:16.5px;font-weight:500">Sed ut perspiciatis</div>
    <div class="abs" style="left:13px;top:282px;display:flex;align-items:center;gap:14px">
      <div class="phone-row" style="font-size:8.5px"><span class="dot" style="width:13px;height:13px"><svg width="7" height="7" viewBox="0 0 10 10"><path d="M2 1l2 2-1 1.5a6 6 0 0 0 2.5 2.5L7 6l2 2-1.5 1.5C4 9 1 6 .5 2.5z" fill="#fff"/></svg></span>+1 555 010 2040</div>
      <div style="font-size:6.5px;font-weight:700;color:#333;display:flex;align-items:center;gap:3px">
        <svg width="6" height="6" viewBox="0 0 6 6"><rect width="6" height="6" rx="1" fill="#165e94"/></svg>Nov 23,2022 &nbsp;|&nbsp;
        <svg width="6" height="6" viewBox="0 0 6 6"><circle cx="3" cy="3" r="3" fill="#165e94"/></svg>04:02pm</div>
    </div>
    <p class="about">Lorem ipsum dolor sit amet, consectetur adipiscing elit, sed do eiusmod tempor incididunt ut labore et dolore magna aliqua. Quis ipsum suspendisse ultrices gravida. Risus commodo viverra maecenas accumsan lacus vel facilisis. Lorem ipsum dolor sit amet, consectetur adipiscing elit,</p>
    <div class="field" style="left:13px;top:422px;width:201px;height:37px;padding:0 15px 0 20px"><span>Checkin</span>
      <svg width="8" height="5" viewBox="0 0 8 5"><path d="M0 0h8L4 5z" fill="#111"/></svg></div>
    <div class="btn" style="left:16px;top:470px;width:196px;height:38px;font-size:11.5px">COURT DATE UPDATES</div>
    <div class="photo" role="img" aria-label="Map showing the check-in GPS location" style="left:16px;top:521px;width:196px;height:109px;border:2px solid #fff;box-shadow:0 1px 4px rgba(0,0,0,.3);border-radius:6px;background:linear-gradient(135deg,#f0e3b0,#e9e9e9 40%,#bfe3a8 70%,#f2e7b8)"></div>
    <div class="abs" style="left:16px;top:655px;font-size:14.5px;font-weight:500">CHECK IN HISTORY</div>
    <ul class="history">
      <li>Lorem ipsum dolor sit ametc</li>
      <li>Onsectetur adipiscing elso eiusmod</li>
      <li>tempor incididunt ut labore</li>
      <li>Et dolore magna aliquuis ipsum</li>
      <li>Suspendisse ultrices gravida.</li>
      <li>Risus commodo viverra maecenas</li>
      <li>accumsan lacus vel facilisis. Lorem</li>
      <li>Isum dolor sit amet, consectetur</li>
      <li>Adipisciorem ipsum dolor sit ametc</li>
      <li>Onsectetur adipiscing elso eiusmod</li>
    </ul>
    <div class="cards">
      <span>Paxa</span><span>Cardia</span><span>Novex</span><span>Amora</span><span>PayLo</span>
    </div>
  </div>
</section>

</body>
</html>
```